Vintage pharmacy themed coffee bag label

This is a coffee label for the signature blend of a medical apothecary (vintage pharmacy) themed coffee company that donates proceeds to fund medical care around the world.

I want the design to scream old/vintage pharmacy such as examples attached (example-asthmacig, citratemagnesia, french-label, witch-sample ). I'd like the label to roughly mimic the setup of the example-asthmacig but with a bit more intricate lettering and design like the other examples have.

Target Market(s)

Higher end coffee drinkers

Industry/Entity Type

It Company

Font styles to use
Serif
Decorative
Script

Colors
191919
7f7f7f
e0e0e0

Requirements
Must have
• The actual text with basic outline is attached as "Actual text for label." I'd like the photo to be of the doctor attached (Dr Fenwick). I also attached the png of the logo to be included on the label with the website right below it
Nice to have
• Colors should be similar to the attached examples. But mostly black/dark brown font with the off white/brown background
Should not have
• nothing that comes to mind

```html
<!DOCTYPE html>
<html lang="en">
<head>
<meta charset="utf-8">
<title>Dr Fenwick's Kavori – Coffee Label</title>
<link rel="stylesheet" href="https://fonts.googleapis.com/css2?family=IM+Fell+Double+Pica+SC&family=Libre+Caslon+Text:wght@700&family=Oswald:wght@400;500&family=Old+Standard+TT&display=swap">
<style>
  :root {
    --ink: #191919;
    --rust: #a23d17;
    --tan-outer: #b98e64;
    --tan-band: #e2bd84;
    --paper-light: #e4cfab;
    --paper-edge: #b88b60;
    --gold: #cfa865;
    --photo-grey: #7f7f7f;
    --photo-light: #e0e0e0;
  }
  * { box-sizing: border-box; margin: 0; padding: 0; }
  html, body { width: 966px; height: 1200px; overflow: hidden; background: var(--tan-outer); }
  .label { position: relative; width: 966px; height: 1200px; background: var(--tan-outer); }
  .label__band { position: absolute; inset: 12px; border: 22px solid var(--tan-band); }
  .label__field {
    position: absolute; inset: 40px;
    border: 3px solid #fff;
    background: radial-gradient(ellipse at 50% 45%, var(--paper-light) 0%, #dcc29b 45%, var(--paper-edge) 100%);
  }
  .label__frame { position: absolute; left: 0; top: 0; }
  .corner { position: absolute; width: 150px; height: 150px;
    background: radial-gradient(circle at 35% 35%, rgba(25,25,25,.55), rgba(25,25,25,.15) 70%, transparent 72%); }
  .corner--tl { left: 40px; top: 40px; }
  .corner--tr { right: 40px; top: 40px; transform: scaleX(-1); }
  .corner--bl { left: 40px; bottom: 40px; transform: scaleY(-1); }
  .corner--br { right: 40px; bottom: 40px; transform: scale(-1,-1); }
  .crest { position: absolute; left: 266px; top: 97px; width: 446px; height: 84px;
    background: linear-gradient(180deg, var(--gold), #a67e45); border-radius: 50% 50% 20% 20% / 60% 60% 30% 30%; opacity: .8; }
  .maker { position: absolute; top: 186px; left: 0; width: 966px; text-align: center;
    font: 700 24px/1 "Libre Caslon Text", serif; color: var(--ink); letter-spacing: .5px; }
  .portrait { position: absolute; left: 386px; top: 216px; width: 198px; height: 285px; border-radius: 50%;
    background: radial-gradient(ellipse at 50% 35%, var(--photo-light) 0%, var(--photo-grey) 55%, #2b2b2b 100%); }
  .product { position: absolute; top: 505px; left: 0; width: 966px; text-align: center;
    font: 400 132px/1 "IM Fell Double Pica SC", serif; color: var(--ink); letter-spacing: 6px; }
  .divider { position: absolute; left: 258px; top: 620px; }
  .claim { position: absolute; top: 668px; left: 0; width: 966px; text-align: center;
    font: 500 22px/1 "Oswald", sans-serif; color: var(--ink); letter-spacing: .2px; }
  .heading { position: absolute; left: 0; width: 966px; text-align: center;
    font: 400 31px/1 "Oswald", sans-serif; color: var(--rust); }
  .heading--ingredients { top: 716px; }
  .heading--directions { top: 777px; }
  .heading--repeat { top: 897px; font-size: 30px; }
  .body-copy { position: absolute; left: 0; width: 966px; text-align: center;
    font: 400 15px/24px "Old Standard TT", serif; font-variant: small-caps; color: var(--ink); letter-spacing: .8px; }
  .body-copy--ingredients { top: 748px; }
  .body-copy--directions { top: 815px; }
  .net-weight { position: absolute; left: 150px; top: 1000px; width: 116px; text-align: center;
    font: 400 22px/34px Arial, sans-serif; color: var(--ink); }
  .brand { position: absolute; left: 326px; top: 995px; width: 318px; text-align: center;
    font: 500 46px/1 "Oswald", sans-serif; color: var(--ink); letter-spacing: 2px; }
  .brand small { display: block; font-size: 18px; letter-spacing: 8px; margin-top: 8px; }
</style>
</head>
<body>
<main class="label">
  <div class="label__band"></div>
  <div class="label__field"></div>
  <svg class="label__frame" width="966" height="1200" viewBox="0 0 966 1200" aria-hidden="true">
    <rect x="52" y="52" width="862" height="1096" fill="none" stroke="#191919" stroke-width="4"/>
    <rect x="59" y="59" width="848" height="1082" fill="none" stroke="#191919" stroke-width="1.5"/>
    <rect x="64" y="64" width="838" height="1072" fill="none" stroke="#191919" stroke-width="1.5"/>
  </svg>
  <div class="corner corner--tl" role="img" aria-label="Ornamental corner scroll"></div>
  <div class="corner corner--tr" role="img" aria-label="Ornamental corner scroll"></div>
  <div class="corner corner--bl" role="img" aria-label="Ornamental corner scroll"></div>
  <div class="corner corner--br" role="img" aria-label="Ornamental corner scroll"></div>

  <div class="crest" role="img" aria-label="Gold acanthus flourish"></div>
  <p class="maker">DR FENWICK’S</p>
  <div class="portrait" role="img" aria-label="Oval portrait photograph of Dr Fenwick"></div>
  <h1 class="product">KAVORI</h1>

  <svg class="divider" width="450" height="24" viewBox="0 0 450 24" aria-hidden="true">
    <g fill="none" stroke="#a23d17" stroke-width="1.5">
      <line x1="20" y1="12" x2="175" y2="12"/>
      <line x1="275" y1="12" x2="430" y2="12"/>
      <path d="M185 12 q20 -10 40 0 q20 10 40 0"/>
      <path d="M185 12 q20 10 40 0 q20 -10 40 0"/>
    </g>
    <g fill="#a23d17">
      <path d="M4 12 l10 -6 l0 12 z"/>
      <path d="M446 12 l-10 -6 l0 12 z"/>
      <circle cx="225" cy="12" r="3"/>
    </g>
  </svg>

  <p class="claim">FOR THE TEMPORARY RELIEF OF PAROXYSMS OF FATIGUE &amp; EXHAUSTION.</p>

  <h2 class="heading heading--ingredients">ACTIVE INGREDIENTS:</h2>
  <p class="body-copy body-copy--ingredients">Iron skillet roasted Ethiopian Yirgacheffe coffee, caffeine</p>

  <h2 class="heading heading--directions">DIRECTIONS:</h2>
  <p class="body-copy body-copy--directions">For pour over variety, mix one part coffee to 10 parts water (i.e. 20g<br>coffee to 200g water). Coffee grounds to approximate table salt and<br>not to exceed in size the head of a pin.</p>

  <h2 class="heading heading--repeat">REPEAT EVERY 4 TO 6 HOURS AS NEEDED</h2>

  <p class="net-weight">NET WT<br>12 oz</p>
  <p class="brand">VESTA<small>COFFEE</small></p>
</main>
</body>
</html>
```